Flyer to Attract New Customers With an Exciting, Proprietary Marketing Plan

Need to prepare an eye catching flyer that will be mailed to all the Embassies and Consultates in the US to announce a new and exciting program dedicated to meeting the travel needs of Ambassadors and staff. Flyer should be eye catching, yet elogant to address the diplomats and should highlight the elements as well as the CEO, Tomas Kerrow and his commitment to incredible customer service

Target Market(s)

Embassies and Consulates of the US

Industry/Entity Type

Travel

Requirements
Must have
• Must have the four elements of the Embassy program (.ppt), photography of the CEO Tomas Kerrow and his commitment to 24/7 service, Overview of the Velmaro, Logo of Velmaro. Be elegant as if presented to a diplomat.
Nice to have
• Call to action....Call 415-682-7150 to book an appointment. Full service travel agency....air, hotel, cars
Should not have
• Be clunky, cluntered, non professional looking, non dignitary

```html
<!DOCTYPE html>
<html lang="en">
<head>
<meta charset="utf-8">
<title>Velmaro Flyer</title>
<link rel="stylesheet" href="https://fonts.googleapis.com/css2?family=Lato:wght@400;700;900&family=Oswald:wght@500&display=swap">
<style>
  :root {
    --orange: #e55a1f;
    --orange-deep: #d8501a;
    --blue: #0d6e9e;
    --navy: #0b5c86;
    --ink: #3a3a3a;
    --paper: #f4f4f4;
    --stage: #8a8a8a;
  }
  * { box-sizing: border-box; margin: 0; padding: 0; }
  html, body { width: 1200px; height: 900px; overflow: hidden; }
  body { background: var(--stage); font-family: "Lato", sans-serif; color: var(--ink); }
  .flyer {
    position: absolute; left: 270px; top: 20px;
    width: 660px; height: 860px;
    background: var(--paper); overflow: hidden;
    box-shadow: 0 6px 20px rgba(0,0,0,.25);
  }
  .hero-bg { position: absolute; left: 0; top: 0; }
  .ceo-photo {
    position: absolute; left: 380px; top: 110px; width: 260px; height: 268px;
    background: linear-gradient(180deg, rgba(229,90,31,0) 0%, #8a5a44 22%, #6e4434 48%, #dfe4ea 62%, #eef1f5 100%);
    border-radius: 130px 130px 0 0;
  }
  .headline {
    position: absolute; left: 40px; top: 48px; width: 270px;
    color: #fff; font-weight: 700; font-size: 31px; line-height: 1.12; text-transform: uppercase;
  }
  .quote {
    position: absolute; left: 40px; top: 245px; width: 220px;
    color: #fff; font-size: 14px; line-height: 1.25; text-transform: uppercase;
  }
  .scene {
    position: absolute; top: 376px; width: 152px; height: 152px; border-radius: 50%;
    border: 5px solid #fff; box-shadow: 0 2px 6px rgba(0,0,0,.2);
  }
  .scene--city { left: 130px; background: linear-gradient(180deg, #a9c6e6 0 55%, #6e7f8f 56% 72%, #7fa7a6 73%); }
  .scene--luggage { left: 304px; background: linear-gradient(180deg, #6f8fb5 0 35%, #e3b27a 36% 55%, #8a4a30 56%); }
  .scene--plane { left: 478px; background: linear-gradient(180deg, #4b86c6 0%, #a9cbe9 60%, #eef3f8 100%); }
  .section-title { color: var(--orange); font-weight: 700; font-size: 19px; text-transform: uppercase; margin-bottom: 10px; }
  .approach { position: absolute; left: 30px; top: 548px; width: 288px; }
  .approach ul { list-style: none; }
  .approach li {
    position: relative; padding-left: 22px; margin-bottom: 7px;
    font-size: 12px; font-weight: 700; line-height: 1.3; color: #333;
  }
  .approach li svg { position: absolute; left: 0; top: 1px; }
  .about { position: absolute; left: 338px; top: 548px; width: 302px; }
  .about p { font-size: 10.5px; line-height: 1.3; margin-bottom: 6px; }
  .brand { position: absolute; left: 20px; top: 772px; display: flex; align-items: flex-start; gap: 12px; }
  .brand-bar { width: 7px; height: 66px; background: var(--navy); }
  .brand-name { font-weight: 900; font-size: 48px; line-height: 1; color: var(--navy); text-transform: lowercase; }
  .brand-tagline { font-size: 16px; color: var(--blue); margin-top: 3px; }
  .contact-band {
    position: absolute; left: 316px; top: 774px; width: 344px; height: 76px;
    background: var(--orange); border-left: 7px solid var(--navy);
    color: #fff; font-family: "Oswald", sans-serif; font-weight: 500; font-size: 17px;
    padding: 10px 22px;
  }
  .contact-band .web { display: block; }
  .contact-band .phone { display: block; text-align: right; margin-top: 14px; }
</style>
</head>
<body>
<main class="flyer">
  <svg class="hero-bg" width="660" height="420" viewBox="0 0 660 420" aria-hidden="true">
    <polygon points="0,0 660,0 660,362 0,392" fill="var(--orange)"/>
    <polygon points="230,388 660,340 660,382 540,388" fill="var(--blue)"/>
    <polygon points="560,385 660,378 660,410 600,410" fill="var(--orange-deep)"/>
  </svg>
  <div class="ceo-photo" role="img" aria-label="Portrait photo of CEO Tomas Kerrow, smiling in a white shirt, committed to 24/7 customer service"></div>

  <h1 class="headline">A new start-up focused on making travel easier</h1>
  <p class="quote">“Simple, no hassles, defers my cash flows.... perfect for my small business”</p>

  <div class="scene scene--city" role="img" aria-label="Photo of a city skyline on the waterfront"></div>
  <div class="scene scene--luggage" role="img" aria-label="Photo of stacked vintage suitcases with a plane at sunset"></div>
  <div class="scene scene--plane" role="img" aria-label="Photo of a passenger jet flying above the clouds"></div>

  <section class="approach">
    <h2 class="section-title">Our Marketing Approach</h2>
    <ul>
      <li><svg width="14" height="14" viewBox="0 0 14 14"><circle cx="7" cy="7" r="6" fill="none" stroke="var(--orange)" stroke-width="1.6"/><path d="M5.5 4.3 8.3 7 5.5 9.7" fill="none" stroke="var(--orange)" stroke-width="1.6"/></svg>Focused on providing an simple and easy booking experience designed to work within your budget and payment preferences</li>
      <li><svg width="14" height="14" viewBox="0 0 14 14"><circle cx="7" cy="7" r="6" fill="none" stroke="var(--orange)" stroke-width="1.6"/><path d="M5.5 4.3 8.3 7 5.5 9.7" fill="none" stroke="var(--orange)" stroke-width="1.6"/></svg>We work diligently but expeditiously to finding you the lowest fare</li>
      <li><svg width="14" height="14" viewBox="0 0 14 14"><circle cx="7" cy="7" r="6" fill="none" stroke="var(--orange)" stroke-width="1.6"/><path d="M5.5 4.3 8.3 7 5.5 9.7" fill="none" stroke="var(--orange)" stroke-width="1.6"/></svg>Putting “Service” Back into Customer Service</li>
      <li><svg width="14" height="14" viewBox="0 0 14 14"><circle cx="7" cy="7" r="6" fill="none" stroke="var(--orange)" stroke-width="1.6"/><path d="M5.5 4.3 8.3 7 5.5 9.7" fill="none" stroke="var(--orange)" stroke-width="1.6"/></svg>Reaching Over 500,000 Customers a Month</li>
    </ul>
  </section>

  <section class="about">
    <h2 class="section-title">About Us</h2>
    <p>Velmaro was founded by a few individuals with many years of experience in the travel industry. We believe our platform is second to none when it comes to airfare affordability.</p>
    <p>Our simple installment payment options gives you the high level of flexibility which is currently not available in the market when it comes to international travel. We have partnered with over 400 airlines to deliver the best prices possible to our customers.</p>
    <p>Our team of travel agents is ready to assist you on the phone you can rest assured we're with you every step of the way to make sure your trip is flawless.</p>
  </section>

  <div class="brand">
    <span class="brand-bar"></span>
    <div>
      <div class="brand-name">Velmaro</div>
      <div class="brand-tagline">Book Now, Pay Later</div>
    </div>
  </div>

  <div class="contact-band">
    <span class="web">WWW.VELMARO.COM</span>
    <span class="phone">CALL US: (415)-682-7150</span>
  </div>
</main>
</body>
</html>
```